Poster design for a company operating care homes in the UK showcasing our core values

We need a poster to display in our care homes showcasing our new core values:

Purpose
We are driven by a clear understanding of why we do what we do: to enrich lives, honour legacies and make a meaningful difference every day, for our residents, their families, our colleagues and our community.

Excellence
We hold ourselves to the highest standards, delivering exceptional care and creating an environment where both residents and staff can thrive.

Openness
We build trust through honest, respectful communication, welcoming feedback, sharing ideas, and embracing change as a path to continuous growth.

Passion
We are passionate about delivering exceptional care. We take pride in what we do and in making a real difference in people’s lives.

Learning
We are committed to personal and professional growth; empowering each other through ongoing development, reflection, and shared knowledge.

Empathy
We actively listen and seek to understand before being understood, recognising the unique stories, feelings, and needs of others.

I have attached a small graphic that we would like you try to incorporate, in addition to our company logo. Please theme the rest of the poster around our company colours.

```html
<!DOCTYPE html>
<html lang="en">
<head>
<meta charset="utf-8">
<title>Core Values Poster</title>
<link rel="stylesheet" href="https://fonts.googleapis.com/css2?family=Poppins:wght@600;700;800&family=Mulish:wght@500&display=swap">
<style>
  :root {
    --navy: #243c5c;
    --navy-deep: #1b2f4b;
    --orange: #e39a72;
    --orange-soft: #eaa984;
    --paper: #f4f5f7;
    --paper-shade: #e6e8ec;
    --white: #ffffff;
  }
  * { margin: 0; padding: 0; box-sizing: border-box; }
  html, body { width: 1200px; height: 929px; overflow: hidden; }
  body { background: var(--paper); }
  .poster {
    position: relative;
    width: 1200px;
    height: 929px;
    overflow: hidden;
    background: linear-gradient(180deg, var(--white) 0%, var(--paper) 55%, var(--paper-shade) 100%);
    font-family: "Mulish", Arial, sans-serif;
    color: var(--navy);
  }
  .arch { position: absolute; inset: 0; }
  .value {
    position: absolute;
    width: 190px;
    text-align: center;
  }
  .value__title {
    font-family: "Poppins", Arial, sans-serif;
    font-weight: 700;
    font-size: 29px;
    line-height: 1.15;
    color: var(--navy);
    margin-bottom: 12px;
  }
  .value__text {
    font-size: 14.5px;
    line-height: 1.35;
    color: var(--navy-deep);
  }
  .value--purpose    { left: 2px;   bottom: 374px; }
  .value--excellence { left: 167px; bottom: 537px; }
  .value--openness   { left: 387px; bottom: 625px; }
  .value--passion    { left: 623px; bottom: 625px; }
  .value--learning   { left: 843px; bottom: 537px; }
  .value--empathy    { left: 1008px; bottom: 374px; }
  .headline {
    position: absolute;
    left: 0; right: 0;
    top: 590px;
    text-align: center;
    font-family: "Poppins", Arial, sans-serif;
    font-weight: 800;
    font-size: 96px;
    line-height: 1;
    letter-spacing: -1px;
    color: var(--white);
  }
  .brand {
    position: absolute;
    left: 0; right: 0;
    top: 790px;
    display: flex;
    justify-content: center;
    align-items: center;
    gap: 16px;
  }
  .brand__mark { width: 34px; height: 34px; background: var(--orange); }
  .brand__name {
    font-family: "Poppins", Arial, sans-serif;
    font-weight: 600;
    font-size: 52px;
    line-height: 1;
    color: var(--navy);
  }
</style>
</head>
<body>
<main class="poster">
  <svg class="arch" width="1200" height="929" viewBox="0 0 1200 929" aria-hidden="true">
    <circle cx="600" cy="1020" r="620" fill="var(--orange)"/>
    <circle cx="600" cy="1020" r="606" fill="var(--navy)"/>
    <circle cx="600" cy="1070" r="345" fill="var(--paper)"/>

    <!-- pointers -->
    <polygon points="74,570 110,570 92,598" fill="var(--navy)"/>
    <polygon points="244,406 280,406 262,434" fill="var(--orange)"/>
    <polygon points="464,318 500,318 482,346" fill="var(--navy)"/>
    <polygon points="700,318 736,318 718,346" fill="var(--orange)"/>
    <polygon points="920,406 956,406 938,434" fill="var(--navy)"/>
    <polygon points="1090,570 1126,570 1108,598" fill="var(--orange)"/>

    <!-- letter badges -->
    <g font-family="Poppins, Arial, sans-serif" font-weight="800" font-size="74" text-anchor="middle">
      <circle cx="92" cy="664" r="64" fill="var(--navy)"/>
      <circle cx="92" cy="664" r="52" fill="none" stroke="var(--white)" stroke-width="2"/>
      <text x="92" y="690" fill="var(--orange)">P</text>

      <circle cx="262" cy="500" r="64" fill="var(--orange)"/>
      <circle cx="262" cy="500" r="52" fill="none" stroke="var(--white)" stroke-width="2"/>
      <text x="262" y="526" fill="var(--navy)">E</text>

      <circle cx="482" cy="411" r="64" fill="var(--navy)"/>
      <circle cx="482" cy="411" r="52" fill="none" stroke="var(--white)" stroke-width="2"/>
      <text x="482" y="437" fill="var(--orange)">O</text>

      <circle cx="718" cy="411" r="64" fill="var(--orange)"/>
      <circle cx="718" cy="411" r="52" fill="none" stroke="var(--white)" stroke-width="2"/>
      <text x="718" y="437" fill="var(--navy)">P</text>

      <circle cx="938" cy="500" r="64" fill="var(--navy)"/>
      <circle cx="938" cy="500" r="52" fill="none" stroke="var(--white)" stroke-width="2"/>
      <text x="938" y="526" fill="var(--orange)">L</text>

      <circle cx="1108" cy="664" r="64" fill="var(--orange)"/>
      <circle cx="1108" cy="664" r="52" fill="none" stroke="var(--white)" stroke-width="2"/>
      <text x="1108" y="690" fill="var(--navy)">E</text>
    </g>
  </svg>

  <section class="value value--purpose">
    <h2 class="value__title">Purpose</h2>
    <p class="value__text">We are driven by a clear understanding of why we do what we do: to enrich lives, honour legacies and make a meaningful difference every day, for our residents, their families, our colleagues and our community.</p>
  </section>
  <section class="value value--excellence">
    <h2 class="value__title">Excellence</h2>
    <p class="value__text">We hold ourselves to the highest standards, delivering exceptional care and creating an environment where both residents and staff can thrive.</p>
  </section>
  <section class="value value--openness">
    <h2 class="value__title">Openness</h2>
    <p class="value__text">We build trust through honest, respectful communication, welcoming feedback, sharing ideas, and embracing change as a path to continuous growth.</p>
  </section>
  <section class="value value--passion">
    <h2 class="value__title">Passion</h2>
    <p class="value__text">We are passionate about delivering exceptional care. We take pride in what we do and in making a real difference in people’s lives.</p>
  </section>
  <section class="value value--learning">
    <h2 class="value__title">Learning</h2>
    <p class="value__text">We are committed to personal and professional growth; empowering each other through ongoing development, reflection, and shared knowledge.</p>
  </section>
  <section class="value value--empathy">
    <h2 class="value__title">Empathy</h2>
    <p class="value__text">We actively listen and seek to understand before being understood, recognising the unique stories, feelings, and needs of others.</p>
  </section>

  <h1 class="headline">CORE VALUES</h1>

  <div class="brand">
    <span class="brand__mark"></span>
    <span class="brand__name">MERIDALE</span>
  </div>
</main>
</body>
</html>
```